Orient Wager Digest Quarterly Magazine

We need a magazine design for a new company based in Asia called Orient Wager Digest (OWD).

OWD provide up to date market information for worldwide executives on relevant gaming issues in Asia, covering:
- specific market and legal challenges
- new regulations and their implications for the
industry
- company operations in different jurisdictions (country specific)
- governance and compliance issues
- financing, HR and technology trends

This magazine design must be high-end and relate more to a business periodical/journal that exhibits reliability and industry expertise than a fashion magazine. For reference purpose see Pivotal Magazine and their previous issue. It is important that this design project has synergy with our previous two magazines (see file uploads).

You can also visit http://www.orientwagerdigest.example, however we are in the process of updating this website.

Initially, we would like to see a conceptual SCAMP for 3 spread layouts, including the following pages:

- Main country page template full-spread (text, image, snippet and data/diagram/graph)
- Editorial page
- Contents page
- Sponsors page
- Front Cover

Specific Requirements:
Page Width = 200mm
Page Height = 265mm
Trim measurement = we usually use 5mm
Corporate Colors = Red #990000, Green #226727
Gutter measurement for a 60 page mag, give or take
(*note that most of the odd pages will be Advertising pages consisting of a full page image, therefore they will not need much work.)
Images can bleed off page

Must Haves:
experience in magazine design
able to work with google drive
able to plot graphs, design diagrams, charts etc...

To All,

Logo version has just been uploaded.

Cheers

```html
<!DOCTYPE html>
<html lang="en">
<head>
<meta charset="utf-8">
<title>China Special Report 2013 – Booming lottery sales</title>
<link href="https://fonts.googleapis.com/css2?family=Bitter:wght@300;400;600&family=Exo+2:wght@400;600&family=Libre+Franklin:wght@400;600&display=swap" rel="stylesheet">
<style>
  :root {
    --paper: #ffffff;
    --ink: #1d1d1b;
    --ink-soft: #5a5a58;
    --title-green: #8ea47f;
    --box-green: #4c5f45;
    --caption-bg: #e8ede6;
    --caption-red: #c8102e;
    --rule: #9a9a9a;
  }
  * { margin: 0; padding: 0; box-sizing: border-box; }
  html, body { width: 906px; height: 1200px; overflow: hidden; background: var(--paper); }
  .page { position: relative; width: 906px; height: 1200px; overflow: hidden; color: var(--ink); }

  .running-head {
    position: absolute; left: 45px; top: 32px;
    font: 600 10px/1 "Exo 2", sans-serif; letter-spacing: 1.2px; color: var(--ink-soft);
  }
  .folio-rule { position: absolute; left: 0; width: 45px; border-top: 2px dotted var(--rule); }
  .folio-rule.top { top: 164px; }
  .folio-rule.bottom { top: 200px; }
  .folio {
    position: absolute; left: 30px; top: 176px;
    font: 400 13px/1 "Exo 2", sans-serif; color: var(--ink);
  }

  .kicker {
    position: absolute; left: 90px; top: 88px;
    font: 400 16px/1 "Libre Franklin", sans-serif; color: var(--ink); letter-spacing: .2px;
  }
  .kicker strong { font-weight: 600; }
  .headline {
    position: absolute; left: 90px; top: 106px;
    font: 600 71px/1 "Bitter", serif; color: var(--title-green); letter-spacing: -1px;
    white-space: nowrap;
  }
  .headline-rule { position: absolute; left: 90px; right: 0; top: 200px; border-top: 2px dotted var(--rule); }
  .byline {
    position: absolute; left: 90px; top: 208px;
    font: 400 11px/1 "Exo 2", sans-serif; letter-spacing: 1px; color: var(--ink);
  }
  .byline b { font-weight: 600; letter-spacing: 1.4px; }

  .feature-photo {
    position: absolute; left: 0; top: 638px; width: 906px; height: 517px;
    background:
      radial-gradient(ellipse 40% 30% at 50% 98%, #b8622a 0%, transparent 70%),
      radial-gradient(ellipse 30% 25% at 78% 68%, #4a3a8c 0%, transparent 70%),
      radial-gradient(ellipse 30% 25% at 12% 70%, #1f5a4a 0%, transparent 70%),
      radial-gradient(ellipse 60% 30% at 50% 8%, #5a6a4e 0%, transparent 75%),
      linear-gradient(180deg, #3a3a30 0%, #6b5d44 35%, #2e3a38 60%, #4a3424 100%);
  }

  .pull-quote {
    position: absolute; left: 90px; top: 278px; width: 263px; height: 397px;
    background: var(--box-green);
    clip-path: polygon(14px 0, calc(100% - 14px) 0, 100% 14px, 100% calc(100% - 14px), calc(100% - 14px) 100%, 14px 100%, 0 calc(100% - 14px), 0 14px);
    padding: 60px 22px 0 29px;
    font: 300 17.5px/24px "Bitter", serif; color: #ffffff;
  }

  .body-column {
    position: absolute; top: 276px; width: 230px;
    font: 300 12px/19.3px "Bitter", serif; color: var(--ink);
    text-align: justify; hyphens: auto; -webkit-hyphens: auto; word-spacing: -0.3px;
  }
  .body-column.first { left: 380px; }
  .body-column.second { left: 630px; }
  .body-column p + p { margin-top: 19.3px; }
  .drop-cap { float: left; font: 300 58px/46px "Bitter", serif; margin: 3px 5px 0 -2px; }

  .caption-box {
    position: absolute; left: 634px; top: 1098px; width: 221px; height: 102px;
    background: var(--caption-bg);
    clip-path: polygon(12px 0, calc(100% - 12px) 0, 100% 12px, 100% 100%, 0 100%, 0 12px);
    padding: 28px 26px 0 20px; text-align: right;
    font: 400 10.5px/15px "Libre Franklin", sans-serif; color: var(--caption-red);
  }
</style>
</head>
<body>
<main class="page">
  <p class="running-head">GEX supplier preview</p>
  <div class="folio-rule top"></div>
  <span class="folio">08</span>
  <div class="folio-rule bottom"></div>

  <p class="kicker"><strong>CHINA</strong> SPECIAL REPORT 2013</p>
  <h1 class="headline">Booming lottery sales</h1>
  <div class="headline-rule"></div>
  <p class="byline">Text by <b>Xxxxxxx Xxxxxxx</b> &nbsp;Photo By <b>Xxxxxx Xxxxxxx</b></p>

  <div class="feature-photo" role="img" aria-label="Wide view of a multi-level circular gaming hall with balconies, themed rooms and rows of machines"></div>

  <aside class="pull-quote">Sed ut perspiciatis unde omnis iste natus error sit voluptatem accusantium dolo remque laudantium. Totam rem aperiam, eaque ipsa quae ab illo inventore veritatis et quasi architecto beatae vitae dicta sunt explicabo.</aside>

  <div class="body-column first">
    <p><span class="drop-cap">S</span>ed ut perspiciatis unde omnis iste natus error sit voluptatem accusantium doloremque laudantium, totam rem aperiam, eaque ipsa quae ab illo inventore veritatis et quasi architecto beatae vitae dicta sunt explicabo.</p>
    <p>Sed ut perspiciatis unde omnis iste natus error sit voluptatem accusantium doloremque laudantium, totam rem aperiam, eaque ipsa quae ab illo inventore veritatis et quasi architecto beatae vitae dicta sunt explicabo. Nemo enim ipsam voluptatem quia voluptas sit aspernatur aut odit aut fugit, sed quia consequuntur magni dolores eos qui ratione voluptatem</p>
  </div>

  <div class="body-column second">
    <p>sequi nesciunt. Neque porro quisquam est, qui dolorem ipsum quia dolor sit amet, consectetur, adipisci velit, sed quia non numquam eius modi tempora incidunt ut labore et dolore magnam aliquam quaerat voluptatem. Ut enim ad minima veniam, quis nostrum exercitationem ullam corporis suscipit laboriosam, nisi ut aliquid ex ea commodi consequatur? Quis autem vel eum iure reprehenderit qui in ea voluptate velit esse quam nihil molestiae consequatur, vel illum qui dolorem eum fugiat quo voluptas nulla pariatur?</p>
    <p>Lorem ipsum dolor sit amet, consectetur adipisicing elit, sed do eiusmod tempor</p>
  </div>

  <p class="caption-box">Lorem ipsum dolor sit amet, consectetur adipisicing elit, sed.</p>
</main>
</body>
</html>
```